Header and Full-Page Flyer needed for 2021 Lone Range Civic Builders Summit

Save the Date Flyer and Header needed for V-OrbMQ's 2021 Lone Range Civic Builders Summit. The Lone Range Civic Builders Summit is developed by Owners, for Owners (and other industry stakeholders.

DO NOT INCLUDE This in your design - for reference on design ideas only.
About the The Lone Range Civic Builders Summit:

Are you working within the boundaries of a smaller town mentality?
Do you feel stuck within your Big City limits?

The Lone Range Civic Builders Summit is where municipalities, counties, ISD's, and other public entities will come together to share what they know, and define what they want to know more about capital project planning design, delivery, and operations.

Font styles to use
Sans Serif

Requirements
Must have
• Lone Range Civic Builders Summit
Date: August 5, 2021
Location: San Antonio, TX

```html
<!DOCTYPE html>
<html lang="en">
<head>
<meta charset="UTF-8">
<title>Save the Date – Lone Range Civic Builders Summit</title>
<link rel="stylesheet" href="https://fonts.googleapis.com/css2?family=Montserrat:wght@400;500;700;800&family=Sacramento&display=swap">
<style>
  :root {
    --green: #8bb33f;
    --navy: #1f3f86;
    --sky: #0a6fba;
    --sky-light: #3b8fcf;
    --ink: #222;
    --frame: #c9c9c9;
    --paper: #ffffff;
  }
  * { margin: 0; padding: 0; box-sizing: border-box; }
  html, body { width: 930px; height: 1200px; overflow: hidden; background: var(--paper); }
  body { position: relative; font-family: "Montserrat", Arial, sans-serif; }

  .flyer {
    position: absolute; left: 106px; top: 92px; width: 717px; height: 1018px;
    border: 1px solid var(--frame); background: var(--paper); overflow: hidden;
  }
  .flyer > * { position: absolute; }

  .save-script {
    left: 38px; top: -18px;
    font-family: "Sacramento", cursive;
    font-size: 250px; line-height: 1; color: var(--green);
    z-index: 2; white-space: nowrap;
  }
  .the-word {
    left: 177px; top: 198px; font-size: 34px; font-weight: 700;
    color: var(--navy); letter-spacing: -1px; z-index: 1;
  }
  .date-word {
    left: 254px; top: 180px; font-size: 80px; font-weight: 800;
    color: var(--navy); letter-spacing: -3px; line-height: 1; z-index: 1;
  }
  .date-divider {
    left: 501px; top: 78px; width: 3px; height: 186px; background: var(--navy);
  }
  .date-day {
    left: 522px; top: 60px; font-size: 132px; font-weight: 800;
    color: var(--green); line-height: 1; letter-spacing: -4px;
  }
  .date-month, .date-year {
    left: 524px; font-size: 42px; font-weight: 700; color: var(--navy);
    line-height: 1; letter-spacing: -1px;
  }
  .date-month { top: 176px; }
  .date-year { top: 222px; }

  .city-band { left: 0; top: 290px; width: 717px; height: 580px; }
  .location {
    left: 0; top: 358px; width: 717px; text-align: center; color: #fff;
  }
  .location-pin { display: block; margin: 0 auto 6px; }
  .location-label { font-size: 25px; font-weight: 500; line-height: 1.1; }
  .location-city { font-size: 38px; font-weight: 700; line-height: 1.25; }

  .summit-name {
    left: 44px; top: 882px; width: 250px;
    font-size: 25px; font-weight: 700; color: var(--navy); line-height: 1.12;
    display: flex; gap: 12px; align-items: flex-start;
  }
  .summit-mark { flex: 0 0 14px; height: 14px; background: var(--green); margin-top: 7px; }
  .footer-divider { left: 310px; top: 890px; width: 2px; height: 102px; background: var(--green); }
  .summit-about {
    left: 327px; top: 899px; width: 350px;
    font-size: 12.6px; line-height: 16.8px; color: var(--ink);
  }
</style>
</head>
<body>
  <main class="flyer">
    <div class="save-script">Save</div>
    <div class="the-word">THE</div>
    <div class="date-word">DATE</div>
    <div class="date-divider"></div>
    <div class="date-day">05</div>
    <div class="date-month">August</div>
    <div class="date-year">2021</div>

    <svg class="city-band" viewBox="0 0 717 580" role="img" aria-label="Photograph of the San Antonio skyline at dusk under a blue sky">
      <defs>
        <linearGradient id="skyFade" x1="0" y1="0" x2="0" y2="1">
          <stop offset="0" stop-color="#0a6fba"/>
          <stop offset="0.45" stop-color="#3b8fcf"/>
          <stop offset="0.72" stop-color="#6f8fa8"/>
          <stop offset="0.9" stop-color="#5a5450"/>
          <stop offset="1" stop-color="#8a7a66"/>
        </linearGradient>
      </defs>
      <path fill="url(#skyFade)" d="
        M0 72 L40 66 L60 70 L110 58 L95 64 L170 50 L200 44 L180 52 L260 36 L330 20
        L310 28 L380 16 L400 22 L470 30 L530 32 L560 28 L620 26 L717 42
        L717 520 L690 530 L650 524 L610 540 L560 548 L520 556 L470 566 L420 570
        L380 578 L330 572 L280 566 L230 572 L180 566 L130 574 L80 566 L40 572 L0 560 Z"/>
      <g stroke="#fff" stroke-width="2" stroke-linecap="round" opacity="0.9">
        <line x1="20" y1="76" x2="70" y2="70"/>
        <line x1="90" y1="70" x2="150" y2="60"/>
        <line x1="210" y1="52" x2="270" y2="42"/>
        <line x1="300" y1="34" x2="360" y2="26"/>
        <line x1="560" y1="36" x2="610" y2="32"/>
        <line x1="480" y1="540" x2="540" y2="532"/>
        <line x1="600" y1="528" x2="660" y2="518"/>
        <line x1="330" y1="560" x2="390" y2="552"/>
      </g>
    </svg>

    <div class="location">
      <svg class="location-pin" width="20" height="28" viewBox="0 0 20 28" aria-hidden="true">
        <path d="M10 0C4.5 0 0 4.4 0 9.8 0 17 10 28 10 28s10-11 10-18.2C20 4.4 15.5 0 10 0z" fill="var(--green)"/>
        <circle cx="10" cy="9.5" r="4" fill="var(--sky)"/>
      </svg>
      <div class="location-label">LOCATION:</div>
      <div class="location-city">SAN ANTONIO, TX</div>
    </div>

    <div class="summit-name"><span class="summit-mark"></span><span>Lone Range Civic Builders Summit</span></div>
    <div class="footer-divider"></div>
    <p class="summit-about">The Lone Range Civic Builders Summit is where municipalities, counties, ISD's, and other public entities will come together to share what they know, and define what they want to know more about capital project planning design, delivery, and operations.</p>
  </main>
</body>
</html>
```